Attention grabbing 6x9 postcard

We are looking to have an attention grabbing post card that be sent out to homeowners from our roofing company Olum Roofing. the concept is that on the front it will say something like (STOP THE KNOCKING!
Tired of roofers knocking on your door? Contact us because we value your time as much as you value the roof over your head."
Olum Roofing
OlumRoofing.com
877.612.OLUM
info@olumroofing.com

Please feel free to come up with something very creative. Once we pick the final design we will provide the copy.

```html
<!DOCTYPE html>
<html lang="en">
<head>
<meta charset="utf-8">
<title>Olum Roofing Postcard</title>
<link rel="stylesheet" href="https://fonts.googleapis.com/css2?family=Anton&family=Barlow+Condensed:wght@500;600;700&family=Montserrat:wght@700;800;900&display=swap">
<style>
:root{
  --yellow:#F8BC0E;
  --black:#111111;
  --white:#ffffff;
  --stage:#8a8a8a;
  --photo-warm:#b08a6a;
  --photo-sky:#6f93b8;
  --photo-roof:#8c8f96;
  --rule:#333333;
}
*{margin:0;padding:0;box-sizing:border-box}
html,body{width:1200px;height:484px;overflow:hidden;background:var(--stage)}
.canvas{position:relative;width:1200px;height:484px}
.card{position:absolute;background:var(--white);overflow:hidden}
.card--front{left:58px;top:72px;width:510px;height:340px}
.card--back{left:632px;top:72px;width:515px;height:342px}
.card-shapes{position:absolute;left:0;top:0}
.abs{position:absolute}

.headline{font-family:"Anton",sans-serif;line-height:1;white-space:nowrap}
.headline--stop{left:252px;top:18px;font-size:62px;color:var(--yellow);-webkit-text-stroke:2.5px var(--black);paint-order:stroke fill;letter-spacing:1px}
.headline--knock{left:254px;top:82px;font-size:56px;color:var(--black)}
.tagline{left:254px;top:143px;font-family:"Barlow Condensed",sans-serif;font-weight:600;font-size:17px;color:var(--black);white-space:nowrap}

.cta-label{font-family:"Montserrat",sans-serif;font-weight:800;color:var(--yellow);letter-spacing:2px;white-space:nowrap;line-height:1}
.card--front .cta-label{left:300px;top:181px;font-size:20px}
.card--back .cta-label{left:18px;top:203px;font-size:17px}

.brand-mark{font-family:"Barlow Condensed",sans-serif;font-weight:700;color:var(--black);text-align:center;line-height:1}
.card--front .brand-mark{left:196px;top:252px;width:76px;font-size:20px}
.card--back .brand-mark{left:300px;top:32px;width:82px;font-size:20px}
.brand-url{font-family:"Montserrat",sans-serif;font-weight:700;color:var(--black);font-size:7.5px;letter-spacing:.3px;white-space:nowrap;text-align:center}
.card--front .brand-url{left:192px;top:383px;width:84px}
.card--front .brand-url{top:383px}
.card--back .brand-url{left:300px;top:83px;width:82px}

.contact-list{list-style:none}
.contact-item{position:absolute;display:flex;align-items:center;gap:8px;font-family:"Anton",sans-serif;color:var(--black);white-space:nowrap;line-height:1}
.contact-item svg{flex:none}
.contact-item--phone{font-size:30px}
.contact-item--line{font-size:17px}

.services-title{left:18px;top:18px;font-family:"Montserrat",sans-serif;font-weight:900;font-size:21px;color:var(--black);line-height:1}
.services-copy{left:18px;top:44px;width:250px;font-family:"Montserrat",sans-serif;font-weight:700;font-size:6.6px;line-height:9.7px;color:var(--black);text-transform:uppercase}
.service-label{top:103px;width:74px;margin-left:-37px;font-family:"Barlow Condensed",sans-serif;font-weight:700;font-size:7.6px;line-height:8.6px;text-align:center;color:var(--black);text-transform:uppercase}
.promise{left:178px;top:199px;font-family:"Barlow Condensed",sans-serif;font-weight:600;font-size:9.5px;line-height:14px;color:var(--black);text-transform:uppercase;white-space:nowrap}

.stamp-box{left:422px;top:15px;width:72px;height:73px;border:1px solid var(--rule)}
.address-line{left:330px;width:163px;height:1px;background:var(--rule)}
</style>
</head>
<body>
<div class="canvas">

  <!-- FRONT -->
  <section class="card card--front">
    <svg class="card-shapes" width="510" height="340" viewBox="0 0 510 340">
      <polygon fill="var(--black)" points="0,0 510,0 510,8 212,8 212,68 119,19 24,70 24,122 0,130"/>
      <polygon fill="var(--yellow)" points="0,220 250,210 490,210 510,191 510,340 0,340"/>
      <polygon class="honeycomb-backdrop" fill="var(--white)" points="119,19 212,68 250,110 250,250 119,330 0,265 0,140 24,77"/>
      <polygon fill="var(--yellow)" points="121,35 204,83 204,179 121,227 38,179 38,83"/>
      <polygon fill="var(--yellow)" points="44,131 82,153 82,197 44,219 6,197 6,153"/>
      <polygon fill="var(--yellow)" points="196,133 234,155 234,199 196,221 158,199 158,155"/>
      <polygon fill="var(--yellow)" points="119,214 161,238 161,286 119,310 77,286 77,238"/>
      <polygon fill="var(--photo-warm)" stroke="var(--black)" stroke-width="1" role="img" aria-label="Photo of a couple on a sofa annoyed by a knock at the door" points="121,51 190,91 190,171 121,211 52,171 52,91"/>
      <polygon fill="var(--photo-sky)" stroke="var(--black)" stroke-width="1" role="img" aria-label="Photo of a blue house with a new roof" points="44,142 73,158.5 73,191.5 44,208 15,191.5 15,158.5"/>
      <polygon fill="#a9b3a0" stroke="var(--black)" stroke-width="1" role="img" aria-label="Photo of a roofing contractor reviewing plans" points="196,144 225,160.5 225,193.5 196,210 167,193.5 167,160.5"/>
      <polygon fill="#9aa07c" stroke="var(--black)" stroke-width="1" role="img" aria-label="Photo of a roofer inspecting shingles" points="119,226 150,244 150,280 119,298 88,280 88,244"/>
      <polygon class="cta-bar" fill="var(--black)" points="254,173 460,173 472,191 460,209 264,209 254,191"/>
      <polygon fill="var(--black)" points="466,173 478,173 490,191 478,209 466,209 478,191"/>
    </svg>

    <div class="abs headline headline--stop">STØP THE</div>
    <div class="abs headline headline--knock">KNOCKING!</div>
    <p class="abs tagline">Tired of roofers knocking on your door</p>
    <div class="abs cta-label">CONTACT US</div>

    <div class="abs brand-mark">OLUM<br>ROOFING</div>
    <div class="abs brand-url" style="top:304px">OLUMROOFING.COM</div>

    <ul class="contact-list">
      <li class="contact-item contact-item--phone" style="left:278px;top:218px">
        <svg width="26" height="26" viewBox="0 0 26 26"><circle cx="13" cy="13" r="13" fill="var(--black)"/><path transform="translate(6 6) scale(.58)" fill="var(--yellow)" d="M6.6 10.8c1.4 2.8 3.8 5.1 6.6 6.6l2.2-2.2c.3-.3.7-.4 1-.2 1.1.4 2.3.6 3.6.6.6 0 1 .4 1 1V20c0 .6-.4 1-1 1C10.6 21 3 13.4 3 4c0-.6.4-1 1-1h3.5c.6 0 1 .4 1 1 0 1.3.2 2.5.6 3.6.1.3 0 .7-.2 1z"/></svg>
        877.612.OLUM
      </li>
      <li class="contact-item contact-item--line" style="left:283px;top:275px">
        <svg width="16" height="16" viewBox="0 0 16 16"><circle cx="8" cy="8" r="8" fill="var(--black)"/><circle cx="8" cy="6" r="2.5" fill="var(--yellow)"/><path d="M3.5 13a4.5 4 0 0 1 9 0z" fill="var(--yellow)"/></svg>
        OLUM ROOFING
      </li>
      <li class="contact-item contact-item--line" style="left:283px;top:298px">
        <svg width="16" height="16" viewBox="0 0 16 16"><circle cx="8" cy="8" r="8" fill="var(--black)"/><circle cx="8" cy="8" r="5" fill="none" stroke="var(--yellow)" stroke-width="1.2"/><ellipse cx="8" cy="8" rx="2" ry="5" fill="none" stroke="var(--yellow)" stroke-width="1.2"/><line x1="3" y1="8" x2="13" y2="8" stroke="var(--yellow)" stroke-width="1.2"/></svg>
        OLUMROOFING.COM
      </li>
      <li class="contact-item contact-item--line" style="left:283px;top:322px">
        <svg width="16" height="16" viewBox="0 0 16 16"><circle cx="8" cy="8" r="8" fill="var(--black)"/><rect x="4" y="5" width="8" height="6" fill="var(--yellow)"/><path d="M4 5l4 3.5L12 5" fill="none" stroke="var(--black)" stroke-width="1"/></svg>
        INFO@OLUMROOFING.COM
      </li>
    </ul>
  </section>

  <!-- BACK -->
  <section class="card card--back">
    <svg class="card-shapes" width="515" height="342" viewBox="0 0 515 342">
      <polygon fill="var(--black)" points="236,0 299,0 261,40"/>
      <line x1="233" y1="0" x2="292" y2="99" stroke="var(--yellow)" stroke-width="2"/>
      <line x1="306" y1="122" x2="336" y2="172" stroke="var(--yellow)" stroke-width="2"/>
      <polygon fill="var(--yellow)" points="0,99 292,99 306,122 0,122"/>
      <polygon fill="var(--yellow)" points="0,172 336,172 238,342 0,342"/>
      <g stroke="var(--yellow)" stroke-width="1.5">
        <line x1="70" y1="158" x2="92" y2="158"/>
        <line x1="144" y1="158" x2="166" y2="158"/>
        <line x1="218" y1="158" x2="240" y2="158"/>
      </g>
      <g stroke="var(--yellow)" stroke-width="3">
        <polygon fill="var(--photo-sky)" role="img" aria-label="Photo of a roof repair with blue underlayment" points="44,128 70,143 70,173 44,188 18,173 18,143"/>
        <polygon fill="#a89a84" role="img" aria-label="Photo of a commercial building roofline" points="118,128 144,143 144,173 118,188 92,173 92,143"/>
        <polygon fill="var(--photo-roof)" role="img" aria-label="Photo of storm damaged shingles" points="192,128 218,143 218,173 192,188 166,173 166,143"/>
        <polygon fill="#9c7a52" role="img" aria-label="Photo of a new house under construction" points="266,128 292,143 292,173 266,188 240,173 240,143"/>
      </g>
      <polygon fill="var(--black)" points="0,196 144,196 152,211.5 144,227 0,227"/>
      <polygon fill="var(--black)" points="148,196 158,196 168,211.5 158,227 148,227 158,211.5"/>
      <polygon fill="var(--black)" points="160,196 168,196 176,211.5 168,227 160,227 168,211.5"/>
    </svg>

    <h2 class="abs services-title">OUR SERVICES</h2>
    <p class="abs services-copy">Olum Roofing offers an array of roofing solutions while providing professional, honest recommendations that address your specific needs. You can always count on us for exceptional service from the moment we meet. From inspection to installation, Olum has you covered.</p>

    <div class="abs service-label" style="left:41px">Repairs &amp;<br>Restoration</div>
    <div class="abs service-label" style="left:120px">Retail/Commercial<br>Roof Replacement</div>
    <div class="abs service-label" style="left:193px">Storm Damage Roof<br>Replacement</div>
    <div class="abs service-label" style="left:265px">New<br>Construction</div>

    <div class="abs cta-label">CONTACT US</div>
    <p class="abs promise">Because we value your time as much as<br>you value the roof over your head</p>

    <ul class="contact-list">
      <li class="contact-item contact-item--phone" style="left:17px;top:233px">
        <svg width="24" height="24" viewBox="0 0 26 26"><circle cx="13" cy="13" r="13" fill="var(--black)"/><path transform="translate(6 6) scale(.58)" fill="var(--yellow)" d="M6.6 10.8c1.4 2.8 3.8 5.1 6.6 6.6l2.2-2.2c.3-.3.7-.4 1-.2 1.1.4 2.3.6 3.6.6.6 0 1 .4 1 1V20c0 .6-.4 1-1 1C10.6 21 3 13.4 3 4c0-.6.4-1 1-1h3.5c.6 0 1 .4 1 1 0 1.3.2 2.5.6 3.6.1.3 0 .7-.2 1z"/></svg>
        877.612.OLUM
      </li>
      <li class="contact-item contact-item--line" style="left:21px;top:266px">
        <svg width="16" height="16" viewBox="0 0 16 16"><circle cx="8" cy="8" r="8" fill="var(--black)"/><circle cx="8" cy="6" r="2.5" fill="var(--yellow)"/><path d="M3.5 13a4.5 4 0 0 1 9 0z" fill="var(--yellow)"/></svg>
        OLUM ROOFING
      </li>
      <li class="contact-item contact-item--line" style="left:21px;top:288px">
        <svg width="16" height="16" viewBox="0 0 16 16"><circle cx="8" cy="8" r="8" fill="var(--black)"/><circle cx="8" cy="8" r="5" fill="none" stroke="var(--yellow)" stroke-width="1.2"/><ellipse cx="8" cy="8" rx="2" ry="5" fill="none" stroke="var(--yellow)" stroke-width="1.2"/><line x1="3" y1="8" x2="13" y2="8" stroke="var(--yellow)" stroke-width="1.2"/></svg>
        OLUMROOFING.COM
      </li>
      <li class="contact-item contact-item--line" style="left:21px;top:310px">
        <svg width="16" height="16" viewBox="0 0 16 16"><circle cx="8" cy="8" r="8" fill="var(--black)"/><rect x="4" y="5" width="8" height="6" fill="var(--yellow)"/><path d="M4 5l4 3.5L12 5" fill="none" stroke="var(--black)" stroke-width="1"/></svg>
        INFO@OLUMROOFING.COM
      </li>
    </ul>

    <div class="abs brand-mark">OLUM<br>ROOFING</div>
    <div class="abs brand-url">OLUMROOFING.COM</div>

    <div class="abs stamp-box"></div>
    <div class="abs address-line" style="top:224px"></div>
    <div class="abs address-line" style="top:250px"></div>
    <div class="abs address-line" style="top:279px"></div>
  </section>

</div>
</body>
</html>
```